Bramwell Quayle Lending Solutions business card design

Need a business card design for my mortgage broking business Bramwell Quayle Lending Solutions.

Target Market(s)

Mortgage clients/colleagues

Industry/Entity Type

Business

Requirements
Must have
• Must utilise logo attached. Possibly have logo only on back of card. my name & contact details on front and something creative?

Must incorporate purple/black/white in colour scheme.

Must incorporate tag line 'The Home Loan Sleuths' under logo - using a script style fint. UPDATE: Mistral doesn't seem to be working on the card. Happy for you to try a different font. preferably a script style font.

Standard business card size.
Nice to have
• Try and incorporate the detective theme - but keep it looking sharp and professional.
Have attached some sample designs - does not have to be this - happy to review any ideas you may have.

```html
<!DOCTYPE html>
<html lang="en">
<head>
<meta charset="utf-8">
<title>Bramwell Quayle Lending Solutions – Business Card</title>
<link rel="stylesheet" href="https://fonts.googleapis.com/css2?family=Open+Sans:ital,wght@0,400;0,600;0,700;1,400&family=Roboto:wght@500;700&display=swap">
<style>
  :root {
    --purple: #4a1c86;
    --purple-dark: #35115f;
    --ink: #2a2a2a;
    --muted: #8a8a8a;
    --card: #f5f5f5;
    --card-edge: #e6e6e6;
    --backdrop: #2f2f2f;
    --white: #ffffff;
  }
  * { box-sizing: border-box; }
  html, body {
    margin: 0;
    width: 1200px;
    height: 900px;
    overflow: hidden;
    background: var(--backdrop);
    font-family: "Open Sans", Arial, sans-serif;
  }
  .stage {
    width: 1200px;
    height: 900px;
    display: flex;
    flex-direction: column;
    align-items: center;
    justify-content: center;
    gap: 40px;
  }
  .card {
    position: relative;
    width: 640px;
    height: 391px;
    background: linear-gradient(160deg, var(--white) 0%, var(--card) 60%, var(--card-edge) 100%);
    overflow: hidden;
    box-shadow: 0 10px 30px rgba(0,0,0,0.45);
  }
  .card svg.shapes {
    position: absolute;
    inset: 0;
    width: 100%;
    height: 100%;
  }

  /* brand name lockup */
  .brand {
    position: absolute;
    display: flex;
    align-items: center;
    gap: 12px;
    color: var(--purple);
    font-family: "Open Sans", Arial, sans-serif;
    font-weight: 700;
    line-height: 1.05;
  }
  .brand-dot {
    border-radius: 50%;
    background: var(--purple);
    flex: none;
  }
  .brand-name span { display: block; }

  /* back of card */
  .card-back .brand {
    left: 0; right: 0;
    top: 100px;
    justify-content: center;
    font-size: 38px;
  }
  .card-back .brand-dot { width: 26px; height: 26px; }
  .tagline-band {
    position: absolute;
    left: 0; right: 0;
    top: 232px;
    height: 56px;
    display: flex;
    align-items: center;
    justify-content: center;
    margin: 0;
    color: var(--white);
    font-family: "Roboto", Arial, sans-serif;
    font-weight: 700;
    font-size: 20px;
    letter-spacing: 4px;
  }

  /* front of card */
  .card-front .brand {
    right: 34px;
    top: 38px;
    font-size: 21px;
    gap: 8px;
  }
  .card-front .brand-dot { width: 14px; height: 14px; }
  .holder {
    position: absolute;
    left: 44px;
    top: 108px;
  }
  .holder-name {
    margin: 0;
    color: var(--purple);
    font-family: "Roboto", Arial, sans-serif;
    font-weight: 700;
    font-size: 27px;
  }
  .holder-role {
    margin: 6px 0 0;
    color: var(--ink);
    font-weight: 700;
    font-size: 13px;
  }
  .holder-speciality {
    margin: 3px 0 0;
    color: var(--muted);
    font-style: italic;
    font-size: 11.5px;
  }
  .contacts {
    position: absolute;
    left: 44px;
    top: 212px;
    margin: 0;
    padding: 0;
    list-style: none;
    color: var(--ink);
    font-size: 13px;
    line-height: 1.35;
  }
  .contacts li {
    display: flex;
    align-items: flex-start;
    gap: 12px;
    margin-bottom: 6px;
  }
  .contacts svg {
    width: 13px;
    height: 13px;
    flex: none;
    margin-top: 2px;
    fill: var(--ink);
  }
</style>
</head>
<body>
<main class="stage">

  <section class="card card-back" aria-label="Back of business card">
    <svg class="shapes" viewBox="0 0 640 391" aria-hidden="true">
      <rect x="0" y="232" width="640" height="56" fill="var(--purple)"/>
      <rect x="0" y="288" width="640" height="4" fill="var(--purple-dark)"/>
    </svg>
    <div class="brand">
      <span class="brand-dot"></span>
      <div class="brand-name">
        <span>Bramwell Quayle</span>
        <span>Lending Solutions</span>
      </div>
    </div>
    <p class="tagline-band">The Home Loan Sleuths</p>
  </section>

  <section class="card card-front" aria-label="Front of business card">
    <svg class="shapes" viewBox="0 0 640 391" aria-hidden="true">
      <polygon points="0,352 640,290 640,300 0,362" fill="var(--card-edge)"/>
      <polygon points="0,362 640,300 640,391 0,391" fill="var(--purple)"/>
      <g class="house-icon" fill="var(--purple)">
        <polygon points="548,302 576,272 604,294 604,297"/>
        <rect x="592" y="262" width="7" height="20"/>
        <rect x="566" y="282" width="6" height="6" fill="var(--white)"/>
        <rect x="574" y="282" width="6" height="6" fill="var(--white)"/>
        <rect x="566" y="290" width="6" height="5" fill="var(--white)"/>
        <rect x="574" y="290" width="6" height="5" fill="var(--white)"/>
      </g>
    </svg>

    <div class="brand">
      <span class="brand-dot"></span>
      <div class="brand-name">
        <span>Bramwell Quayle</span>
        <span>Lending Solutions</span>
      </div>
    </div>

    <div class="holder">
      <h1 class="holder-name">Clarissa Vane</h1>
      <p class="holder-role">Managing Director</p>
      <p class="holder-speciality">Non-Conforming Mortgage Specialists</p>
    </div>

    <ul class="contacts">
      <li>
        <svg viewBox="0 0 16 16" aria-label="Phone"><rect x="4" y="1" width="8" height="14" rx="1.5"/><rect x="5.5" y="3" width="5" height="8" fill="var(--white)"/></svg>
        <span>0400 555 218</span>
      </li>
      <li>
        <svg viewBox="0 0 16 16" aria-label="Email"><rect x="1" y="3" width="14" height="10" rx="1"/><polyline points="1.5,4 8,9 14.5,4" fill="none" stroke="var(--white)" stroke-width="1.4"/></svg>
        <span>clarissa@bramwellloans.com.au</span>
      </li>
      <li>
        <svg viewBox="0 0 16 16" aria-label="Website"><circle cx="8" cy="8" r="7"/><ellipse cx="8" cy="8" rx="3" ry="7" fill="none" stroke="var(--white)" stroke-width="1"/><line x1="1" y1="8" x2="15" y2="8" stroke="var(--white)" stroke-width="1"/></svg>
        <span>www.bramwellloans.com.au</span>
      </li>
      <li>
        <svg viewBox="0 0 16 16" aria-label="Address"><path d="M8 1a5 5 0 0 0-5 5c0 4 5 9 5 9s5-5 5-9a5 5 0 0 0-5-5z"/><circle cx="8" cy="6" r="2" fill="var(--white)"/></svg>
        <span>Quill House, Level 1, 214<br>Larkspur Lane Melbourne 3000</span>
      </li>
    </ul>
  </section>

</main>
</body>
</html>
```